RLTP Business Card Design

I have a rough idea of the design / layout of the company business card but need help in finalizing the design and quality.

I'm looking for the card to be stand out, but simple, on the front with clear detail on the back with space for some one to write any other detail they need onto the card. The rough draft includes the crinkled graph paper back ground which I quite like for the front.

I will need the card design completed and ready to print in Australian business card standard sizes. This includes detail on all colors, fonts and type faces used as well as copy of the original for editing (inserting other employee details).

I have included the company logo and a rough draft of the card, including the graphic I would like to use for the back ground on the front, I am not sure that the graphic is any good for printing, not the highest res.

Thanks,

Owen

```html
<!DOCTYPE html>
<html lang="en">
<head>
<meta charset="utf-8">
<title>RLTP Business Card</title>
<link rel="stylesheet" href="https://fonts.googleapis.com/css2?family=Michroma&family=Exo+2:wght@400;600&display=swap">
<style>
  :root {
    --stage: #e6e6e6;
    --silver-light: #f4f4f4;
    --silver-mid: #d9d9d9;
    --silver-dark: #bdbdbd;
    --ink: #1c1c1c;
    --band: #161616;
    --band-edge: #3a3a3a;
    --paper-text: #2a2a2a;
    --muted: #7a7a7a;
    --white: #f5f5f5;
  }
  * { box-sizing: border-box; margin: 0; padding: 0; }
  html, body { width: 1200px; height: 750px; overflow: hidden; }
  body {
    background: var(--stage);
    font-family: "Exo 2", sans-serif;
    position: relative;
  }
  .card {
    position: absolute;
    top: 216px;
    width: 520px;
    height: 318px;
    border-radius: 26px;
    overflow: hidden;
    background: linear-gradient(135deg, var(--silver-light), var(--silver-mid) 70%, var(--silver-dark));
    box-shadow: 0 8px 22px rgba(0,0,0,0.18);
  }
  .card--front { left: 60px; }
  .card--back { left: 620px; }
  .card__shape { position: absolute; inset: 0; width: 100%; height: 100%; }

  .brand { position: absolute; font-family: "Michroma", sans-serif; color: var(--ink); }
  .brand__name { display: block; line-height: 1; letter-spacing: 2px; }
  .brand__tagline { display: block; text-transform: uppercase; letter-spacing: 1px; white-space: nowrap; }

  .card--front .brand { left: 44px; top: 58px; }
  .card--front .brand__name { font-size: 92px; }
  .card--front .brand__tagline { font-size: 12.5px; margin-top: 8px; }

  .card--back .brand { left: 28px; top: 84px; }
  .card--back .brand__name { font-size: 40px; }
  .card--back .brand__tagline { font-size: 6.5px; margin-top: 4px; }

  .brand-ghost {
    position: absolute;
    right: -20px; top: 60px;
    font-family: "Michroma", sans-serif;
    font-size: 150px;
    line-height: 1;
    color: #ffffff;
    opacity: 0.06;
    letter-spacing: 4px;
  }

  .person { position: absolute; right: 28px; top: 22px; text-align: right; font-family: "Michroma", sans-serif; color: var(--ink); }
  .person__name { font-size: 17px; letter-spacing: 1px; text-transform: uppercase; }
  .person__role { font-size: 8px; letter-spacing: 2px; text-transform: uppercase; margin-top: 3px; color: var(--paper-text); }

  .contact { position: absolute; display: flex; align-items: flex-start; gap: 8px; color: var(--white); font-size: 12.5px; line-height: 1.35; }
  .contact__icon { width: 18px; height: 18px; flex: none; }
  .contact--address { left: 28px; top: 170px; }
  .contact--phone { left: 230px; top: 90px; }
  .contact--email { left: 362px; top: 90px; }
  .contact--social { left: 362px; top: 178px; }
  .contact--web { left: 28px; top: 272px; color: var(--muted); }
</style>
</head>
<body>

<section class="card card--front" aria-label="Card front">
  <svg class="card__shape" viewBox="0 0 520 318" preserveAspectRatio="none" aria-hidden="true">
    <defs>
      <linearGradient id="front-band" x1="0" y1="0" x2="1" y2="0">
        <stop offset="0" stop-color="#2c2c2c"/>
        <stop offset="0.6" stop-color="#141414"/>
        <stop offset="1" stop-color="#050505"/>
      </linearGradient>
    </defs>
    <path d="M0,262 C150,262 330,245 430,190 C470,168 500,140 520,118 L520,318 L0,318 Z" fill="url(#front-band)"/>
    <path d="M0,262 C150,262 330,245 430,190 C470,168 500,140 520,118" fill="none" stroke="#8a8a8a" stroke-width="1.2" opacity="0.6"/>
  </svg>
  <div class="brand">
    <span class="brand__name">RLTP</span>
    <span class="brand__tagline">Real Light Tone Production .com.au</span>
  </div>
</section>

<section class="card card--back" aria-label="Card back">
  <svg class="card__shape" viewBox="0 0 520 318" preserveAspectRatio="none" aria-hidden="true">
    <defs>
      <linearGradient id="back-band" x1="0" y1="0" x2="1" y2="1">
        <stop offset="0" stop-color="#262626"/>
        <stop offset="1" stop-color="#080808"/>
      </linearGradient>
    </defs>
    <path d="M0,150 L180,150 C215,150 220,72 260,72 L520,72 L520,252 L0,252 Z" fill="url(#back-band)"/>
  </svg>
  <div class="brand-ghost" aria-hidden="true">RLTP</div>

  <div class="brand">
    <span class="brand__name">RLTP</span>
    <span class="brand__tagline">Real Light Tone Production .com.au</span>
  </div>

  <div class="person">
    <p class="person__name">Owen Marsh</p>
    <p class="person__role">Director</p>
  </div>

  <div class="contact contact--address">
    <svg class="contact__icon" viewBox="0 0 18 18" aria-hidden="true">
      <circle cx="9" cy="9" r="9" fill="#5a5a5a"/>
      <path d="M9 3.8a3.2 3.2 0 0 0-3.2 3.2c0 2.4 3.2 6.2 3.2 6.2s3.2-3.8 3.2-6.2A3.2 3.2 0 0 0 9 3.8z" fill="#f0f0f0"/>
      <circle cx="9" cy="7" r="1.2" fill="#5a5a5a"/>
    </svg>
    <p>27 Harbour Lane Bayview,<br>NSW 2104</p>
  </div>

  <div class="contact contact--phone">
    <svg class="contact__icon" viewBox="0 0 18 18" aria-hidden="true">
      <circle cx="9" cy="9" r="9" fill="#5a5a5a"/>
      <path d="M6.2 4.6l1.6 1.9-.9 1.2c.6 1.3 1.6 2.3 2.9 2.9l1.2-.9 1.9 1.6-.8 1.4c-3.6-.3-6.4-3.1-6.7-6.7z" fill="#f0f0f0"/>
    </svg>
    <p>555 0142 77</p>
  </div>

  <div class="contact contact--email">
    <svg class="contact__icon" viewBox="0 0 18 18" aria-hidden="true">
      <circle cx="9" cy="9" r="9" fill="#5a5a5a"/>
      <rect x="4.5" y="5.8" width="9" height="6.4" rx="0.8" fill="#f0f0f0"/>
      <path d="M4.8 6.2L9 9.4l4.2-3.2" fill="none" stroke="#5a5a5a" stroke-width="0.9"/>
    </svg>
    <p>owen@rltp.example</p>
  </div>

  <div class="contact contact--social">
    <svg class="contact__icon" viewBox="0 0 18 18" aria-hidden="true">
      <circle cx="9" cy="9" r="9" fill="#5a5a5a"/>
    </svg>
    <p>social.example/rltp</p>
  </div>

  <div class="contact contact--web">
    <svg class="contact__icon" viewBox="0 0 18 18" aria-hidden="true">
      <circle cx="9" cy="9" r="9" fill="#9a9a9a"/>
      <path d="M6.5 5.5L12.5 9l-6 3.5z" fill="#f0f0f0"/>
    </svg>
    <p>www.rltp.example</p>
  </div>
</section>

</body>
</html>
```